Bright Harbor Design

We need a web design for our startup company based in Zurich, Switzerland called Bright Harbor. We offer professional flirt and dating advice, self development with seminars and practical coachings.

The final website aims for two capital goals. First, it will contain text, pictures and video based content presenting and advertising our services. Furthermore, we want to bind our costumers with a plattform offering them to share their expiriences related with our services.

The targeted group will be men from 25 to 40 years.
Updates

The design requires also a register-box to put in the clients Name and Email

I need (besides of the "email registration box") a "Video Gallery", "Blog" and "Agenda (with the next events to come)"

Target Market(s)

Guys around 25 to 40 years who want to improve their social lifestyle

Industry/Entity Type

Advertising

Requirements
Must have
• First and foremost, the design must transfer strong emotions and suggest an attractive social lifestyle.

The design should not be overloaded with content but should include pictures, videos and text.

The design should present a modern, urban lifestyle.
Nice to have
• There is a logo attached to the assignement. However, if you have a good idea for an improved or different logo, please do not hesitate to design your ideas.

```html
<!DOCTYPE html>
<html lang="en">
<head>
<meta charset="utf-8">
<title>Bright Harbor – Self development, flirt and dating advice</title>
<link rel="stylesheet" href="https://fonts.googleapis.com/css2?family=Open+Sans:ital,wght@0,300;0,400;0,600;0,700;1,700&display=swap">
<style>
  :root {
    --teal: #00936f;
    --teal-dark: #007a5c;
    --harbor-blue: #1f7fa6;
    --ink: #3c3c3c;
    --white: #ffffff;
    --field-top: #e6e6e6;
    --field-bottom: #f3f3f3;
    --field-border: #cfcfcf;
    --hero-a: #b9b2a8;
    --hero-b: #7d8a97;
    --hero-c: #2c2a2c;
  }
  * { box-sizing: border-box; margin: 0; padding: 0; }
  html, body { width: 1200px; height: 700px; overflow: hidden; }
  body { font-family: "Open Sans", Arial, sans-serif; background: var(--white); position: relative; }

  .site-header {
    position: absolute; top: 0; left: 0; width: 1200px; height: 70px;
    background: linear-gradient(#ffffff, #f7f7f7);
    z-index: 2;
  }
  .brand {
    position: absolute; left: 130px; top: 22px;
    display: flex; align-items: center; gap: 8px;
    color: var(--teal); font-weight: 600; font-size: 19px; letter-spacing: 0.2px;
  }
  .brand-dot { width: 14px; height: 14px; border-radius: 50%; background: var(--teal); }
  .main-nav { position: absolute; top: 29px; left: 627px; display: flex; }
  .main-nav a {
    color: var(--ink); text-decoration: none; font-size: 13px; margin-right: 29px;
  }
  .main-nav a:last-child { margin-right: 0; }
  .nav-active-tab { position: absolute; left: 612px; top: 58px; }

  .hero {
    position: absolute; top: 70px; left: 0; width: 1200px; height: 630px;
    background:
      radial-gradient(ellipse 260px 340px at 880px 300px, rgba(230,205,190,0.55), transparent 70%),
      radial-gradient(ellipse 320px 420px at 1050px 320px, var(--hero-c), transparent 75%),
      radial-gradient(ellipse 260px 360px at 470px 380px, rgba(225,215,205,0.9), transparent 75%),
      linear-gradient(90deg, var(--hero-b) 0%, var(--hero-a) 45%, #9a8f86 70%, #3a3639 100%);
  }

  .hero-mark {
    position: absolute; top: 132px; left: 0; width: 1200px; text-align: center;
    color: var(--white); font-weight: 600; font-size: 20px;
  }
  .hero-title {
    position: absolute; top: 186px; left: 0; width: 1200px; text-align: center;
    color: var(--white); font-weight: 300; font-size: 44px; line-height: 50px;
  }
  .hero-title em { font-style: italic; font-weight: 700; }
  .hero-lead {
    position: absolute; top: 350px; left: 0; width: 1200px; text-align: center;
    color: var(--white); font-weight: 300; font-size: 25px;
  }
  .hero-lead strong { font-weight: 600; }
  .hero-divider { position: absolute; top: 400px; left: 270px; }

  .register-box {
    position: absolute; top: 459px; left: 270px; width: 660px; height: 70px;
    background: var(--white); border-radius: 8px;
    display: flex; align-items: center; padding: 0 20px; gap: 20px;
  }
  .register-field {
    width: 220px; height: 34px; border-radius: 10px;
    border: 1px solid var(--field-border);
    background: linear-gradient(var(--field-top), var(--field-bottom));
    box-shadow: inset 0 2px 3px rgba(0,0,0,0.12);
    font-family: inherit; font-size: 13px; color: #999; padding: 0 12px;
  }
  .register-field::placeholder { color: #999; }
  .register-button {
    width: 140px; height: 34px; border: none; border-radius: 8px;
    background: linear-gradient(var(--teal), var(--teal-dark));
    color: var(--white); font-family: inherit; font-weight: 600; font-size: 13px;
  }

  .scroll-hint {
    position: absolute; top: 580px; left: 0; width: 1200px; text-align: center;
    color: var(--white); font-size: 15px; font-weight: 300;
  }
  .scroll-mouse { position: absolute; top: 610px; left: 585px; }
</style>
</head>
<body>
  <header class="site-header">
    <div class="brand"><span class="brand-dot"></span>Bright Harbor</div>
    <nav class="main-nav">
      <a href="#">Services</a>
      <a href="#">About Us</a>
      <a href="#">Agenda</a>
      <a href="#">Video Gallery</a>
      <a href="#">Blog</a>
      <a href="#">Contacts</a>
    </nav>
    <svg class="nav-active-tab" width="78" height="12" viewBox="0 0 78 12">
      <path d="M2 12 C10 2, 68 2, 76 12 Z" fill="var(--harbor-blue)"/>
    </svg>
  </header>

  <section class="hero" role="img" aria-label="Blurred photo of a smiling young man and a dark-haired woman sitting together in an urban cafe"></section>

  <div class="hero-mark">Bright Harbor</div>
  <h1 class="hero-title">Self development, flirt and dating advice with<br><em>Bright Harbor…</em></h1>
  <p class="hero-lead">Share your <strong>experience</strong> - register for <strong>FREE</strong>!</p>
  <svg class="hero-divider" width="660" height="24" viewBox="0 0 660 24">
    <path d="M0 3 H312 L330 21 L348 3 H660" fill="none" stroke="rgba(255,255,255,0.75)" stroke-width="1"/>
  </svg>

  <form class="register-box">
    <input class="register-field" type="text" placeholder="Name">
    <input class="register-field" type="email" placeholder="E-Mail">
    <button class="register-button" type="button">REGISTER</button>
  </form>

  <div class="scroll-hint">Scroll down</div>
  <svg class="scroll-mouse" width="30" height="54" viewBox="0 0 30 54">
    <rect x="1" y="1" width="28" height="44" rx="12" fill="var(--white)"/>
    <rect x="11" y="8" width="8" height="18" rx="4" fill="none" stroke="#b8b8b8" stroke-width="2"/>
    <path d="M11 46 L15 52 L19 46 Z" fill="var(--white)"/>
  </svg>
</body>
</html>
```